Business Card
Larkframe, LLC
Professional
Omar Pettis
Founder and CEO
412 Birchwell Rd
Springfield, NJ 07134
omar.pettis@larkframe.com
www.larkframe.com
I am open on the font choice. A different font may be used if it works visually.
Nothing
Illustrator file of our Corporate Logo

```html
<!DOCTYPE html>
<html lang="en">
<head>
<meta charset="utf-8">
<title>Larkframe, LLC — Business Card</title>
<link rel="stylesheet" href="https://fonts.googleapis.com/css2?family=Didact+Gothic&family=Questrial&display=swap">
<style>
  :root {
    --backdrop: #2e2e2e;
    --card-white: #ffffff;
    --brand-blue: #1d5fae;
    --navy: #1e2f5a;
    --green-light: #b9d85a;
    --green-deep: #8cbf2e;
    --blue-light: #2aa6e0;
    --blue-deep: #0d4f96;
    --accent-yellow: #f2e94a;
    --text-white: #ffffff;
    --mark-grey: #c9ced6;
  }
  * { margin: 0; padding: 0; box-sizing: border-box; }
  html, body {
    width: 1200px;
    height: 937px;
    overflow: hidden;
    background: var(--backdrop);
  }
  .card {
    position: absolute;
    left: 100px;
    top: 163px;
    width: 1000px;
    height: 610px;
    border-radius: 28px;
    overflow: hidden;
    background: var(--card-white);
    box-shadow: 0 10px 30px rgba(0,0,0,0.45);
    font-family: "Didact Gothic", "Questrial", sans-serif;
  }
  .card-bands {
    position: absolute;
    inset: 0;
    width: 100%;
    height: 100%;
  }
  .brand {
    position: absolute;
    left: 78px;
    top: 44px;
    display: flex;
    align-items: center;
  }
  .brand-dot {
    width: 180px;
    height: 180px;
    border-radius: 50%;
    background: var(--mark-grey);
    flex: none;
  }
  .brand-text {
    margin-left: 22px;
  }
  .brand-name {
    font-size: 100px;
    line-height: 1;
    color: var(--brand-blue);
    letter-spacing: -1px;
  }
  .brand-tagline {
    margin-top: 8px;
    margin-left: 34px;
    font-size: 26px;
    color: var(--navy);
    letter-spacing: 0.3px;
  }
  .person {
    position: absolute;
    left: 75px;
    top: 284px;
    color: var(--text-white);
  }
  .person-name {
    font-size: 44px;
    line-height: 1.1;
    -webkit-text-stroke: 0.8px var(--text-white);
  }
  .person-title {
    font-size: 30px;
    line-height: 1.3;
  }
  .contact {
    position: absolute;
    left: 75px;
    top: 448px;
    right: 70px;
    color: var(--text-white);
    font-size: 28px;
    line-height: 40px;
  }
  .contact-label {
    color: var(--accent-yellow);
  }
  .contact-last {
    display: flex;
    justify-content: space-between;
  }
  .website {
    color: var(--accent-yellow);
    -webkit-text-stroke: 0.5px var(--accent-yellow);
  }
</style>
</head>
<body>
  <div class="card">
    <svg class="card-bands" viewBox="0 0 1000 610" preserveAspectRatio="none" aria-hidden="true">
      <defs>
        <linearGradient id="greenBand" x1="0" y1="0" x2="1" y2="0">
          <stop offset="0" stop-color="var(--green-deep)"/>
          <stop offset="0.6" stop-color="var(--green-light)"/>
          <stop offset="1" stop-color="#eef5d4"/>
        </linearGradient>
        <linearGradient id="blueBand" x1="0" y1="0" x2="0" y2="1">
          <stop offset="0" stop-color="var(--blue-light)"/>
          <stop offset="1" stop-color="var(--blue-deep)"/>
        </linearGradient>
      </defs>
      <rect x="0" y="266" width="1000" height="344" fill="url(#greenBand)"/>
      <polygon points="0,426 1000,298 1000,610 0,610" fill="url(#blueBand)"/>
    </svg>

    <div class="brand">
      <div class="brand-dot"></div>
      <div class="brand-text">
        <div class="brand-name">Larkframe</div>
        <div class="brand-tagline">Frame Stories • Move Audiences</div>
      </div>
    </div>

    <div class="person">
      <div class="person-name">Omar Pettis</div>
      <div class="person-title">Founder and CEO</div>
    </div>

    <div class="contact">
      <div class="address">412 Birchwell Rd Springfield, NJ 07134</div>
      <div class="phone"><span class="contact-label">Phone:</span> 862-555-0147</div>
      <div class="contact-last">
        <span class="email"><span class="contact-label">Email:</span>&nbsp; omar.pettis@larkframe.com</span>
        <span class="website">www.larkframe.com</span>
      </div>
    </div>
  </div>
</body>
</html>
```